Wanted: A Simple yet Awesome Blog Hero Image

We need a hero image (blog graphic header) to replace our existing one: https://www.brantwellsupply.com//blog/soil-classification-foundation-and-pavement-design-starts-here
Want something to reflect what the blog article is about and is a reflection of the title.

Note: we are not in love with any of our hero graphics

Industry/Entity Type

Construction

Colors

Designer to choose colors to be used in the design.

Requirements
Must have
• Width must be 715px
• Height must not exceed 400px
• Content on graphic should be: Soil Classification: Foundation and Pavement Design Starts Here
Nice to have
• a product shown that is mentioned in the blog
Should not have
• a product with a Carraway logo

```html
<!DOCTYPE html>
<html lang="en">
<head>
<meta charset="utf-8">
<title>Soil Classification — Foundation &amp; Pavement Design Starts Here</title>
<link rel="stylesheet" href="https://fonts.googleapis.com/css2?family=Montserrat:wght@700&family=Open+Sans:wght@300;700&display=swap">
<style>
  :root {
    --soil-top: #93603d;
    --soil-mid: #74462a;
    --soil-deep: #4a2815;
    --soil-base: #2b170b;
    --strip: #1f1109;
    --divider: rgba(255, 235, 215, 0.18);
    --title-fill: rgba(120, 74, 44, 0.55);
    --title-edge: rgba(255, 230, 205, 0.55);
    --subtitle: #eadbcb;
    --label: #ffffff;
    --metal-light: #d9dadd;
    --metal-dark: #8f9196;
    --chart: #c9c4bb;
  }
  * { margin: 0; padding: 0; box-sizing: border-box; }
  html, body { width: 1200px; height: 671px; overflow: hidden; background: var(--soil-base); }
  .hero {
    position: relative;
    width: 1200px;
    height: 671px;
    overflow: hidden;
    background: linear-gradient(180deg, var(--soil-top) 0%, var(--soil-mid) 40%, var(--soil-deep) 72%, var(--soil-base) 100%);
  }
  .soil-layers { position: absolute; inset: 0; }
  .hero-title {
    position: absolute;
    top: 40px;
    left: 0;
    width: 100%;
    text-align: center;
    font-family: "Montserrat", sans-serif;
    font-weight: 700;
    font-size: 78px;
    letter-spacing: 3px;
    color: var(--title-fill);
    -webkit-text-stroke: 1.5px var(--title-edge);
    text-shadow: 0 3px 6px rgba(40, 18, 6, 0.45);
  }
  .hero-subtitle {
    position: absolute;
    top: 144px;
    left: 0;
    width: 100%;
    text-align: center;
    font-family: "Open Sans", sans-serif;
    font-weight: 300;
    font-size: 29px;
    color: var(--subtitle);
  }
  .product-strip {
    position: absolute;
    left: 0;
    top: 607px;
    width: 100%;
    height: 64px;
    background: var(--strip);
  }
  .strip-divider {
    position: absolute;
    top: 0;
    left: 956px;
    width: 1px;
    height: 671px;
    background: var(--divider);
  }
  .product-image {
    position: absolute;
    border-radius: 10px;
  }
  .product-image.tips { left: 37px; top: 420px; width: 206px; height: 75px; background: linear-gradient(90deg, #7a2a30, var(--metal-light) 45%, var(--metal-dark)); opacity: .85; }
  .product-image.rod { left: 59px; top: 574px; width: 139px; height: 17px; background: linear-gradient(180deg, var(--metal-light), var(--metal-dark)); border-radius: 6px; }
  .product-image.sieves { left: 294px; top: 470px; width: 243px; height: 142px; background: radial-gradient(ellipse at 50% 45%, #c4c6ca, var(--metal-dark)); border-radius: 50%; }
  .product-image.chart-book { left: 646px; top: 428px; width: 213px; height: 188px; background: linear-gradient(90deg, #e6e3de, var(--chart) 50%, #a88a5c); border-radius: 4px; }
  .product-image.stack { left: 965px; top: 420px; width: 210px; height: 184px; background: linear-gradient(180deg, var(--metal-light), var(--metal-dark)); border-radius: 16px; }
  .product-label {
    position: absolute;
    transform: translateX(-50%);
    white-space: nowrap;
    font-family: "Open Sans", sans-serif;
    font-weight: 700;
    font-size: 13px;
    color: var(--label);
  }
</style>
</head>
<body>
<div class="hero">
  <svg class="soil-layers" width="1200" height="671" viewBox="0 0 1200 671" aria-hidden="true">
    <path d="M0 110 C200 90 420 125 640 108 S1000 92 1200 112 L1200 671 L0 671 Z" fill="#84532f" opacity="0.55"/>
    <path d="M0 250 C240 236 480 268 720 250 S1040 238 1200 255 L1200 671 L0 671 Z" fill="#6a3e22" opacity="0.6"/>
    <path d="M0 360 C260 350 520 375 780 362 S1060 352 1200 366 L1200 671 L0 671 Z" fill="#55301a" opacity="0.6"/>
    <path d="M0 440 C220 432 500 452 760 440 S1060 432 1200 445 L1200 671 L0 671 Z" fill="#3c2010" opacity="0.6"/>
  </svg>

  <h1 class="hero-title">SOIL CLASSIFICATION</h1>
  <p class="hero-subtitle">Foundation &amp; Pavement Design Starts Here</p>

  <div class="product-strip"></div>
  <div class="strip-divider"></div>

  <div class="product-image tips" role="img" aria-label="Pocket penetrometer adapter tips"></div>
  <span class="product-label" style="left:143px; top:507px;">POCKET PENETROMETER</span>

  <div class="product-image rod" role="img" aria-label="Pocket penetrometer"></div>
  <span class="product-label" style="left:143px; top:621px;">POCKET PENETROMETER</span>

  <div class="product-image sieves" role="img" aria-label="Stainless steel test sieves"></div>
  <span class="product-label" style="left:416px; top:621px;">TEST SIEVE</span>

  <div class="product-image chart-book" role="img" aria-label="Open book of soil color charts"></div>
  <span class="product-label" style="left:747px; top:621px;">SOIL COLOR CHARTS</span>

  <div class="product-image stack" role="img" aria-label="Stack of test sieves with pan and lid"></div>
  <span class="product-label" style="left:1065px; top:621px;">POCKET PENETROMETER</span>
</div>
</body>
</html>
```